Larkfield Advisory Group LLC Business Card Design

I'm looking for a fresh, sharp, clean and current/modern format for my company. This is a start up in the professional services (security/risk management consulting) industry. Catering to C-suite executives as well as senior director types of halcyon 800 companies.

Target Market(s)

Halcyon 800 companies and their C-suite staff with particular focus on VP of Human Resources and Director of Security.

Industry/Entity Type

Business

Font styles to use
Serif

Colors
0455a3
9bcb3c
acd037
3377b5
eaf1f7

Requirements
Must have
• Fresh, sharp, clean and current/modern look and feel.

```html
<!DOCTYPE html>
<html lang="en">
<head>
<meta charset="utf-8">
<title>Larkfield Advisory Group – Business Card</title>
<link rel="stylesheet" href="https://fonts.googleapis.com/css2?family=Arimo:wght@400;700&display=swap">
<style>
  :root {
    --navy: #0f2a5c;
    --green: #6a9a2c;
    --card: #f4f4f2;
    --ink-soft: #2a3a5c;
    --backdrop: #e6e4df;
  }
  * { box-sizing: border-box; margin: 0; padding: 0; }
  html, body {
    width: 1200px; height: 900px; overflow: hidden;
    background: var(--backdrop);
    font-family: "Arimo", Arial, sans-serif;
  }
  .stage { position: relative; width: 1200px; height: 900px; }

  .card {
    position: absolute;
    background: var(--card);
    box-shadow: 0 2px 6px rgba(0,0,0,.12);
  }
  .card--back  { left: 80px;  top: 70px;  width: 520px; height: 315px; }
  .card--front { left: 420px; top: 410px; width: 700px; height: 424px; }

  .mark-dot {
    display: inline-block; border-radius: 50%;
    background: var(--navy);
  }
  .brand-name {
    color: var(--navy); font-weight: 700;
    text-transform: uppercase; letter-spacing: .02em; line-height: 1.05;
  }

  .tagline {
    display: flex; align-items: center; gap: 10px;
    color: var(--green); font-weight: 700;
    text-transform: uppercase; letter-spacing: .04em;
    white-space: nowrap;
  }
  .tagline::before, .tagline::after {
    content: ""; height: 1.5px; background: var(--green); flex: 1;
  }

  /* back face */
  .back-lockup {
    position: absolute; left: 0; right: 0; top: 82px;
    display: flex; flex-direction: column; align-items: center; gap: 14px;
  }
  .back-lockup .mark-dot { width: 64px; height: 64px; }
  .back-lockup .brand-name { font-size: 24px; text-align: center; }
  .card--back .tagline {
    position: absolute; left: 140px; right: 140px; top: 250px; font-size: 13px;
  }

  /* front face */
  .front-lockup {
    position: absolute; left: 48px; top: 120px;
    display: flex; align-items: center; gap: 18px;
  }
  .front-lockup .mark-dot { width: 78px; height: 78px; }
  .front-lockup .brand-name { font-size: 27px; }
  .card--front .tagline {
    position: absolute; left: 144px; top: 212px; width: 240px; font-size: 12.5px;
  }

  .contact {
    position: absolute; left: 430px; top: 60px;
    font-size: 14px; font-style: normal; color: var(--ink-soft); line-height: 1.45;
  }
  .contact-row { display: flex; gap: 10px; }
  .contact-label { color: var(--green); width: 10px; }
  .contact-address { margin-top: 12px; }
  .contact-rule { height: 1.5px; background: var(--green); margin: 10px 0 8px; width: 230px; }
  .contact-web { color: var(--navy); font-size: 15px; }

  .person { position: absolute; left: 48px; bottom: 62px; color: var(--navy); }
  .person-name { font-size: 30px; font-weight: 400; text-transform: uppercase; letter-spacing: .01em; }
  .person-role { font-size: 17px; color: var(--ink-soft); margin-top: 2px; }
</style>
</head>
<body>
<main class="stage">

  <section class="card card--back" aria-label="Card back">
    <div class="back-lockup">
      <span class="mark-dot" aria-hidden="true"></span>
      <span class="brand-name">Larkfield Advisory Group</span>
    </div>
    <p class="tagline">Clear, Calm &amp; Ready</p>
  </section>

  <section class="card card--front" aria-label="Card front">
    <div class="front-lockup">
      <span class="mark-dot" aria-hidden="true"></span>
      <span class="brand-name">Larkfield<br>Advisory Group</span>
    </div>
    <p class="tagline">Clear, Calm &amp; Ready</p>

    <address class="contact">
      <div class="contact-row"><span class="contact-label">T</span><span>01632 960418</span></div>
      <div class="contact-row"><span class="contact-label">F</span><span>01632 960427</span></div>
      <div class="contact-row"><span class="contact-label">E</span><span>hello@larkfieldadvisory.co.uk</span></div>
      <div class="contact-address">12 Mill Reach, Eastbrook<br>Westshire, EB4 7QT</div>
      <div class="contact-rule"></div>
      <div class="contact-web">www.larkfieldadvisory.co.uk</div>
    </address>

    <div class="person">
      <p class="person-name">Owen Halbrook</p>
      <p class="person-role">Development Manager</p>
    </div>
  </section>

</main>
</body>
</html>
```